Velmora Suites Collection

I'm looking for a four page graphic design (home page, search summary/results page, apartment details page, generic information page for content such as FAQ and thank you for submitting forms etc). The pages will be used to develop a web application to promote serviced apartments throughout Africa. Although the business is based in Africa, apartments will be offered to clients across the globe. Apartments will also be situated worldwide.

Target Market(s)

Target audience is business and individual travellers looking for short stays in apartments worldwide.

Number of Pages Required

4 pages

Requirements
Must have
• Clean professional design

```html
<!DOCTYPE html>
<html lang="en">
<head>
<meta charset="utf-8">
<title>Velmora Suites Collection</title>
<link href="https://fonts.googleapis.com/css2?family=Cinzel:wght@400;700&family=Arimo:wght@400;700&family=Tinos:wght@400;700&display=swap" rel="stylesheet">
<style>
:root{
  --sky:#5ba3f0;
  --sky-light:#8ec0f5;
  --navy:#2c5683;
  --navy-deep:#24476f;
  --blue-text:#2f6fc4;
  --orange:#d9731f;
  --rust:#8c3a12;
  --nav-text:#5a1e06;
  --white:#ffffff;
  --grey-text:#444;
  --muted:#8a8a8a;
  --rule:#a9cdf3;
}
*{margin:0;padding:0;box-sizing:border-box}
html,body{width:991px;height:1200px;overflow:hidden}
body{position:relative;background:linear-gradient(90deg,var(--navy-deep),var(--navy) 10%,var(--navy) 90%,var(--navy-deep));font-family:Arimo,Arial,sans-serif;color:var(--grey-text)}
.abs{position:absolute}
.topbar{left:0;top:0;width:991px;height:43px;background:var(--sky);border-bottom:1px solid #4a8fdc}
.clock{left:368px;top:9px;width:415px;height:23px;background:#4c93e4;border:1px solid #3a7fd0;color:#e9f3ff;font-size:12px;line-height:21px;padding-left:8px;white-space:nowrap}
.clock b{color:#fff}
.clock span{opacity:.55;margin:0 6px}
.btn-top{top:9px;height:23px;background:#4c93e4;border:1px solid #2e6cb8;color:#fff;font-family:Tinos,serif;font-size:13px;line-height:21px;text-align:center}
.hero{left:61px;top:43px;width:870px;height:182px;background:linear-gradient(100deg,#3b2a22 0%,#7a4a2c 30%,#c9a27a 48%,#e7d6bf 58%,#8a5a36 75%,#3a2a22 100%)}
.hero-pager{left:813px;top:180px;width:80px;height:19px;background:rgba(0,0,0,.45);color:#999;font-size:12px;line-height:19px;text-align:center}
.brand-box{left:106px;top:32px;width:216px;height:114px;background:linear-gradient(#fafafa,#e2e2e2);border:1px solid #ccc;text-align:center;font-family:Cinzel,serif;color:#333;box-shadow:0 2px 5px rgba(0,0,0,.3)}
.brand-box .l1{font-size:30px;margin-top:14px;line-height:32px}
.brand-box .l2{font-size:20px;line-height:26px}
.brand-box .rule{width:148px;height:1px;background:#555;margin:6px auto 8px}
.brand-box .l3{font-size:12px;letter-spacing:6px;padding-left:6px}
.nav{left:61px;top:225px;width:870px;height:39px;background:linear-gradient(#e07a34,#c85f22);display:flex;border-bottom:1px solid #a54a16}
.nav a{font-family:Tinos,serif;font-size:15px;color:var(--nav-text);text-decoration:none;line-height:39px;letter-spacing:.4px;border-right:1px solid #b85620;text-align:center;white-space:nowrap}
.nav a:last-child{border:0}
.nav a.current{color:#7a3a1a;opacity:.8}
.nav-caret{left:116px;top:253px}
.page{left:61px;top:264px;width:870px;height:762px;background:var(--white)}
.dropdown{left:587px;top:265px;width:191px;height:103px;background:var(--rust);z-index:3}
.dropdown div{height:34px;line-height:34px;padding-left:9px;font-family:Tinos,serif;font-size:14px;color:#f5dccb;border-bottom:1px solid #6f2c0c}
.dropdown div:last-child{border:0}
.search{left:70px;top:273px;width:471px;height:312px;background:linear-gradient(#c8650f,var(--orange) 12%,#d97b24);padding:6px}
.panel-title{font-family:Cinzel,serif;font-size:25px;line-height:28px;height:44px;padding:9px 0 0 8px;white-space:nowrap}
.panel-title b{font-weight:700}
.search .panel-title{color:#5a2506}
.search-body{background:#fff;position:absolute;left:9px;top:49px;width:453px;height:254px}
.label{font-size:15px;color:var(--blue-text);position:absolute}
.field{position:absolute;height:22px;border:1px solid #b8c7d8;background:#fff}
.field.select::after{content:"";position:absolute;right:2px;top:2px;width:15px;height:16px;background:#c9dbf1;border:1px solid #7ea3cf}
.chev{position:absolute;right:5px;top:8px;width:0;height:0;border-left:4px solid transparent;border-right:4px solid transparent;border-top:5px solid #2b5c9f;z-index:1}
.cal{position:absolute;width:21px;height:17px}
.btn-search{position:absolute;left:11px;top:220px;width:65px;height:23px;background:linear-gradient(#4e93e2,#2f6ec2);border:1px solid #2a5ea6;color:#fff;font-family:Tinos,serif;font-size:13px;line-height:21px;text-align:center}
.intro{left:556px;top:275px;width:358px}
.intro h1{font-weight:400;font-size:25px;line-height:28px;color:var(--blue-text);height:56px}
.intro p{font-size:12.6px;line-height:18px;color:#444;margin-top:26px}
.see{font-family:Tinos,serif;font-size:13px;color:var(--muted)}
.intro .see{display:block;margin-top:13px;padding-bottom:9px;border-bottom:1px solid var(--rule)}
.news{left:70px;top:607px;width:472px;height:345px;background:linear-gradient(#5aa2ef,#4b95e8)}
.news .panel-title{color:#234a7a;padding-left:10px}
.news-body{position:absolute;left:6px;top:39px;width:460px;height:300px;background:#fff;padding:0 10px}
.item{border-bottom:1px solid var(--rule);padding-bottom:10px}
.item h2{font-weight:400;font-size:22px;color:var(--orange);margin-top:10px;line-height:26px}
.item time{display:block;font-size:11.5px;color:#e48a2c;margin-top:12px}
.item p{font-size:12.6px;line-height:18px;color:#444;margin-top:8px}
.item .see{display:block;line-height:16px}
.all-news{text-align:right;margin-top:8px;padding-right:2px}
.best{left:556px;top:607px;width:198px;height:345px;background:linear-gradient(#c8650f,var(--orange))}
.best .panel-title{color:#5a2506;padding-left:9px}
.best-body{position:absolute;left:5px;top:40px;width:188px;height:299px;background:#fff}
.thumb{position:absolute;left:8px;width:76px;height:48px}
.thumb-text{position:absolute;left:98px;font-size:12.6px;line-height:18px;color:var(--blue-text)}
.promo{background:linear-gradient(#4b8fdb,#2f6cc0);border:1px solid #3b7bd0;text-align:center;font-family:Cinzel,serif;overflow:hidden}
.promo .art{position:absolute}
.promo-offers{left:771px;top:607px;width:140px;height:166px}
.promo-dest{left:770px;top:788px;width:140px;height:165px}
.promo .small{color:#fff;font-size:14px;font-weight:700}
.promo .big{color:#bad9fb;font-size:28px;line-height:28px}
.promo .big2{color:#163d73;font-size:28px;line-height:28px}
.footer{left:0;top:1026px;width:991px;height:143px;background:linear-gradient(#2d72cf 0,#2d72cf 6px,#5499ea 7px,#6aaaf2)}
.foot-brand{left:73px;top:1054px;width:180px;text-align:center;font-family:Cinzel,serif;color:#e9f2ff}
.foot-brand .l1{font-size:32px;line-height:34px}
.foot-brand .l2{font-size:23px;line-height:30px}
.foot-brand .rule{width:176px;height:1px;background:#d6e6fb;margin:5px auto 10px}
.foot-brand .l3{font-size:13px;letter-spacing:6px;padding-left:6px;white-space:nowrap}
.foot-divider{left:269px;top:1047px;width:1px;height:108px;background:#9cc6f5}
.address{right:63px;top:1059px;text-align:right;font-family:Tinos,serif;font-size:12px;line-height:18px;color:#9fc8f5;font-style:normal}
.foot-nav{left:294px;top:1136px;display:flex;gap:29px}
.foot-nav a{font-family:Tinos,serif;font-size:14.5px;color:#183e6f;text-decoration:none;letter-spacing:.5px}
.legal{left:0;top:1169px;width:991px;height:31px;background:var(--sky-light);font-family:Tinos,serif;font-size:11px;color:#4d6f99;line-height:31px;text-align:right;padding-right:68px;word-spacing:1px}
</style>
</head>
<body>

<div class="abs topbar"></div>
<div class="abs clock"><b>Friday 13 November 2009</b><span>|</span>Sydney 15:01<span>|</span>Beijing 13:01<span>|</span>Tokyo 14:01</div>
<div class="abs btn-top" style="left:790px;width:64px">Log in</div>
<div class="abs btn-top" style="left:864px;width:65px">Register</div>

<div class="abs hero" role="img" aria-label="Photo of a warmly lit serviced apartment lounge with sofa, lamps and kitchen counter"></div>
<div class="abs hero-pager">&#9664;&nbsp; 3/12 &nbsp;&#9654;</div>

<div class="abs brand-box">
  <div class="l1">Velmora</div>
  <div class="l2">Suites</div>
  <div class="rule"></div>
  <div class="l3">COLLECTION</div>
</div>

<nav class="abs nav">
  <a class="current" style="width:129px">REGISTER</a>
  <a style="width:177px">OUR SERVICES</a>
  <a style="width:220px">OUR DESTINATIONS</a>
  <a style="width:191px">SPECIAL OFFERS</a>
  <a style="width:153px">CONTACT US</a>
</nav>
<svg class="abs nav-caret" width="12" height="7" viewBox="0 0 12 7"><path d="M0 7 L6 0 L12 7Z" fill="#5a1e06"/></svg>

<div class="abs page"></div>

<div class="abs dropdown">
  <div>Option 1</div><div>Option 2</div><div>Option 3</div>
</div>

<section class="abs search">
  <div class="panel-title"><b>APARTMENTS</b> SEARCH</div>
  <div class="search-body">
    <span class="label" style="left:14px;top:21px">Country</span>
    <span class="label" style="left:240px;top:21px">Destination</span>
    <div class="field select" style="left:12px;top:42px;width:203px"><i class="chev"></i></div>
    <div class="field select" style="left:238px;top:42px;width:203px"><i class="chev"></i></div>
    <span class="label" style="left:14px;top:87px">Arrival Date</span>
    <span class="label" style="left:239px;top:87px">Return Date</span>
    <div class="field" style="left:12px;top:108px;width:177px"></div>
    <svg class="cal" style="left:196px;top:111px" viewBox="0 0 21 17"><rect x=".5" y=".5" width="20" height="16" fill="#cfe2fa" stroke="#3c7ad0"/><rect x=".5" y=".5" width="20" height="4" fill="#3c7ad0"/><path d="M2 8h17M2 11h17M2 14h17M5 5v11M8 5v11M11 5v11M14 5v11M17 5v11" stroke="#5a92dc" stroke-width=".8"/></svg>
    <div class="field" style="left:238px;top:108px;width:177px"></div>
    <svg class="cal" style="left:422px;top:111px" viewBox="0 0 21 17"><rect x=".5" y=".5" width="20" height="16" fill="#cfe2fa" stroke="#3c7ad0"/><rect x=".5" y=".5" width="20" height="4" fill="#3c7ad0"/><path d="M2 8h17M2 11h17M2 14h17M5 5v11M8 5v11M11 5v11M14 5v11M17 5v11" stroke="#5a92dc" stroke-width=".8"/></svg>
    <span class="label" style="left:14px;top:145px">Numbers of Travelers</span>
    <div class="field select" style="left:12px;top:173px;width:101px"><i class="chev"></i></div>
    <div class="btn-search">Search</div>
  </div>
</section>

<article class="abs intro">
  <h1>Lorem ipsum dolor sit amet, consectetur adipiscing elit.</h1>
  <p>Duis a adipiscing risus. Sed tortor neque, laoreet ut varius at, rutrum non nibh. In hac habitasse platea dictumst. Integer facilisis dictum risus, non laoreet purus semper in. Nulla dui urna, lobortis nec eleifend at, consequat sed nisi. Quisque sagittis diam vitae diam congue vel venenatis lectus elementum. Nunc elementum, lorem eu luctus tincidunt, massa lorem tincidunt justo, ornare sollicitudin sem odio volutpat dolor. Donec a orci magna. Phasellus sapien dui, mollis vel accumsan vel, venenatis sed nibh. Nulla in luctus lacus. Cras eu magna tortor, vel pharetra magna. Sed vel hendrerit nisi. Etiam sed augue turpis.</p>
  <span class="see">See more</span>
</article>

<section class="abs news">
  <div class="panel-title"><b>LATEST</b> NEWS</div>
  <div class="news-body">
    <div class="item">
      <h2>Lorem ipsum dolor</h2>
      <time>11 - Nov - 09</time>
      <p>Duis a adipiscing risus. Sed tortor neque, laoreet ut varius at, rutrum non nibh. In hac habitasse platea dictumst. Integer facilisis dictum risus, non</p>
      <span class="see">See more</span>
    </div>
    <div class="item">
      <h2>Lorem ipsum dolor</h2>
      <time>08 - Nov - 09</time>
      <p>Duis a adipiscing risus. Sed tortor neque, laoreet ut varius at, rutrum non nibh. In hac habitasse platea dictumst. Integer facilisis dictum risus, non</p>
      <span class="see">See more</span>
    </div>
    <div class="see all-news">See all news</div>
  </div>
</section>

<section class="abs best">
  <div class="panel-title"><b>THE</b> BEST</div>
  <div class="best-body">
    <div class="thumb" style="top:8px;background:linear-gradient(135deg,#8a6b55,#e8e2da 60%,#6d5a4a)" role="img" aria-label="Photo of a bright apartment living room"></div>
    <div class="thumb-text" style="top:5px">Quisque<br>sagittis diam</div>
    <div class="thumb" style="top:66px;background:linear-gradient(135deg,#c9b79a,#f4f1ec 55%,#9a8870)" role="img" aria-label="Photo of a bedroom with white linen"></div>
    <div class="thumb-text" style="top:70px">diam vitae</div>
    <div class="thumb" style="top:125px;background:linear-gradient(135deg,#5a5a22,#c8c070 50%,#3d4a2a)" role="img" aria-label="Photo of a lounge with green armchairs"></div>
    <div class="thumb-text" style="top:129px">diam vitae</div>
    <div class="thumb" style="top:184px;background:linear-gradient(135deg,#7a4a1a,#e0a050 50%,#6a3a12)" role="img" aria-label="Photo of a warm lit hotel bedroom"></div>
    <div class="thumb-text" style="top:188px">Quisque<br>sagittis diam</div>
    <div class="thumb" style="top:243px;background:linear-gradient(135deg,#4a3a2a,#d9cbb5 50%,#8a6a4a)" role="img" aria-label="Photo of a kitchen counter with breakfast"></div>
    <div class="thumb-text" style="top:247px">sagittis diam</div>
  </div>
</section>

<div class="abs promo promo-offers">
  <div class="art" style="left:12px;top:10px;width:86px;height:66px;border-radius:40px 10px 40px 10px;background:linear-gradient(135deg,#ff5a4a,#c2121a)" role="img" aria-label="Illustration of a red sale tag"></div>
  <div style="position:absolute;left:0;right:0;top:86px">
    <div class="small" style="padding-left:28px">SEE OUR</div>
    <div class="big">SPECIAL</div>
    <div class="big2">OFFERS</div>
  </div>
</div>

<div class="abs promo promo-dest">
  <div class="art" style="left:10px;top:8px;width:118px;height:98px;border-radius:50%;background:radial-gradient(#f5e23a,#e0a81a 60%,rgba(47,108,192,0) 72%)" role="img" aria-label="Illustration of a small yellow propeller plane"></div>
  <div style="position:absolute;left:0;right:0;top:114px">
    <div class="big" style="color:#d2e6fd">SEE OUR</div>
    <div style="color:#d2e6fd;font-size:14px;line-height:18px;white-space:nowrap">DESTINATIONS</div>
  </div>
</div>

<footer class="abs footer"></footer>
<div class="abs foot-brand">
  <div class="l1">Velmora</div>
  <div class="l2">Suites</div>
  <div class="rule"></div>
  <div class="l3">COLLECTION</div>
</div>
<div class="abs foot-divider"></div>
<address class="abs address">
  Adress: Nam volutpat, sapien nec posuere fringilla, orci erat dictum<br>
  Vivamus volutpat lacinia ante, ac iaculis nisl pellentesque at<br>
  Tel: +99 (9) 99 9999 9999 &nbsp; Fax: +99 (9) 99 9999 9999
</address>
<nav class="abs foot-nav">
  <a>HOME</a><a>OUR SERVICES</a><a>OUR DESTINATIONS</a><a>SPECIAL OFFERS</a><a>CONTACT US</a>
</nav>
<div class="abs legal">© 2009 Velmora Suites Collection &nbsp;&nbsp;&nbsp;&nbsp; Legal politics</div>

</body>
</html>
```